Need a clean & modern homepage for an education site + opportunity for longer term work

Thanks for viewing our project. We are excited about this new website and we hope that we might build a relationship with designers as we work on this project. I provided quite a few details and requirements to help you more quickly create a design that meets our needs.
Who we are:
We are a website that discusses the importance of college accreditation and provides a directory of college programs.
What we need:
A homepage that meets the below requirements and is inspired by the examples provided
Definition of accredited:
ac·cred·it·ed [uh-kred-i-tid] adj.
1. officially recognized as meeting the essential requirements, as of academic excellence: accredited schools.
2. provided with official credentials, as by a government: an accredited diplomatic representative.
3. accepted as authoritative: an accredited theory.
Overall look and feel for the homepage:
- Clean, simple and modern
- Limited (or zero) pictures
- Utilize color blocks with text
- A trend seems to be longer vertical length homepages with lots of whitespace. I generally like this trend as long as the page is not way to tall.
Inspirations: Sites that have a similar look and feel to what I need.
http://lernvista.org/
http://www.campusmetrix.com/colleges/orlen-university/
http://quietmarrow.org/
http://www.velmoratalent.com/
http://www.pluvo.com/
http://sketches.zumo.com/
Items to be included on the homepage. Details below on each item.
- Top navigation
- Logo: Please leave a blank area for a logo. The logo has not been designed.
- Simple graphic/color block at the top that highlights a definition of “Accredited” – the definition should be formatted like it is being copy/pasted from a dictionary.
- Space for a video and small (50 word) written description of the video. You can use placeholder text.
- One section with 3 Paragraphs of content (each paragraph around 100 words) with a header at the top. You can use placeholder text but please create the formatting. At the end of the 3 paragraphs please have a “Read More” Note this shouldn't be 3 separate paragraphs with three read mores - it is 3 paragraphs with one read more at the end.
- An area with the header “Search Colleges by State” that has anchor text links to all 50 states.
Top navigation:
- Home
- States – with a subnav dropdown that includes all 50 US states.
- Programs – with a subnav dropdown that includes program titles (list below)
- Degrees - with a subnav dropdown that includes 5 degree levels (list below)
- Accreditation – no subnav
- Rankings – no subnav
- Resources – no subnav
Footer
- Link to about us, privacy, and a copyright www.url.com
Programs List for sub navigation
Accounting
Art
Bible
Business
Criminal Justice
Design
Engineering
English
Law
LPN to RN
Management
Math
MBA
MPH
Medical Assisting
Military
Nursing
Occupational Therapy
Paralegal
Psychology
Pharmacy
RN to BSN
Radiology
Social Work
Sonography
Degrees list for sub navigation
Certificate
Associate
Bachelors
Masters
PhD
Thanks so much - looking forward to working with you!

```html
<!DOCTYPE html>
<html lang="en">
<head>
<meta charset="utf-8">
<title>AccredHub Online – Home</title>
<link rel="stylesheet" href="https://fonts.googleapis.com/css2?family=Montserrat:wght@400;600;700;800&family=Source+Sans+3:ital,wght@0,400;0,600;1,400&display=swap">
<style>
:root{
  --blue:#1a9bef;
  --blue-deep:#0d86dc;
  --blue-light:#4fb6f5;
  --ink:#2b2f33;
  --text:#555b61;
  --muted:#8a9096;
  --white:#ffffff;
  --pale:#eef1f4;
  --trust:#ececec;
  --dark:#333538;
  --dark-text:#d7d9db;
  --footer:#f1f2f3;
}
*{box-sizing:border-box;margin:0;padding:0}
html,body{width:1200px;height:3396px;overflow:hidden}
body{font-family:"Source Sans 3",Arial,sans-serif;color:var(--text);background:var(--white);position:relative}
section,header,footer{position:absolute;left:0;width:1200px}
a{color:inherit;text-decoration:none}
h2{font-family:"Montserrat",Arial,sans-serif;font-weight:800;text-transform:uppercase;text-align:center;letter-spacing:.5px}

/* header */
.site-header{top:0;height:140px;background:var(--blue)}
.logo{position:absolute;left:40px;top:22px;font-family:"Montserrat",Arial,sans-serif;font-weight:800;font-size:38px;line-height:38px;color:var(--white)}
.social{position:absolute;right:36px;top:22px;display:flex;gap:10px}
.social span{width:34px;height:34px;background:var(--white);border-radius:3px;display:block}
.main-nav{position:absolute;right:36px;top:92px;display:flex;gap:26px;font-family:"Montserrat",Arial,sans-serif;font-weight:700;font-size:16px;color:var(--white);letter-spacing:.3px}
.main-nav .has-sub::after{content:"";display:inline-block;margin-left:6px;border:5px solid transparent;border-top-color:var(--white);vertical-align:-1px}

/* definition */
.definition{top:140px;height:240px}
.word{position:absolute;left:116px;top:24px}
.word h1{font-family:"Montserrat",Arial,sans-serif;font-weight:600;font-size:50px;color:var(--ink);letter-spacing:1px}
.word .say{font-style:italic;color:var(--blue);font-size:38px;margin-top:-2px}
.word .pos{font-style:italic;color:var(--muted);font-size:22px;margin-top:14px}
.senses{position:absolute;left:560px;top:26px;width:590px;list-style:none;font-size:22px;line-height:30px;color:var(--ink)}
.senses li{margin-bottom:18px}

/* features */
.features{top:330px;height:500px}
.features svg.band{position:absolute;top:0;left:0}
.feature-row{position:absolute;top:140px;left:0;width:1200px;display:flex;justify-content:center;gap:120px}
.feature{width:260px;text-align:center;color:var(--white)}
.feature svg{height:64px}
.feature h3{font-family:"Montserrat",Arial,sans-serif;font-weight:800;font-size:28px;margin:18px 0 12px}
.feature p{font-size:16px;line-height:20px;opacity:.92}
.btn{display:inline-block;font-family:"Montserrat",Arial,sans-serif;font-weight:700;font-size:14px;letter-spacing:1px;padding:12px 28px;border-radius:3px}
.btn-white{background:var(--white);color:var(--blue-deep);margin-top:22px}
.btn-outline{border:2px solid var(--white);color:var(--white)}

/* video */
.video{top:830px;height:530px}
.video h2{margin-top:82px;font-size:40px;color:var(--ink)}
.video-text{position:absolute;left:134px;top:202px;width:340px;font-size:17px;line-height:24px}
.player{position:absolute;left:560px;top:160px;width:500px;height:300px;background:#222;border-radius:4px;overflow:hidden}
.player .still{position:absolute;inset:0 0 40px 0;background:linear-gradient(135deg,#6e6a63,#a39c90 55%,#5d5a55)}
.player .play{position:absolute;left:224px;top:104px;width:52px;height:52px;background:var(--white);border-radius:4px}
.player .play::after{content:"";position:absolute;left:20px;top:15px;border:11px solid transparent;border-left:16px solid #333;border-right:0}
.controls{position:absolute;left:0;bottom:0;width:100%;height:40px;background:#1e1e1e}
.controls .track{position:absolute;left:14px;right:80px;top:18px;height:5px;background:#555;border-radius:3px}
.controls .track i{display:block;width:24%;height:100%;background:var(--blue);border-radius:3px}
.controls .knob{position:absolute;left:118px;top:14px;width:12px;height:12px;border-radius:50%;background:var(--white)}
.controls .vol{position:absolute;right:40px;top:15px;width:20px;height:10px;background:#aaa}
.controls .full{position:absolute;right:14px;top:13px;width:14px;height:14px;border:2px solid #aaa}

/* trust */
.trust{top:1360px;height:140px;background:var(--trust)}
.trust .label{position:absolute;left:134px;top:52px;font-family:"Montserrat",Arial,sans-serif;font-size:30px;color:#6b6f73;letter-spacing:1px}
.badge{position:absolute;top:50px;height:40px;background:#cfd1d3;border-radius:3px}

/* paragraphs */
.paragraphs{top:1500px;height:510px;background:var(--blue)}
.paragraphs h2{margin-top:64px;font-size:40px;color:var(--white)}
.paragraphs .copy{position:absolute;left:134px;top:152px;width:932px;color:var(--white);font-size:16px;line-height:22px}
.paragraphs .copy p{margin-bottom:30px}
.paragraphs .btn-outline{position:absolute;left:512px;top:404px}

/* states */
.states{top:2010px;height:550px;background:var(--pale)}
.states .map{position:absolute;left:170px;top:50px;width:860px;height:460px;border-radius:46% 40% 38% 30% / 30% 36% 50% 44%;background:linear-gradient(160deg,#bfe1f8,#d6ecfb 60%,#c8e5f9)}
.states h2{position:relative;margin-top:90px;font-size:36px;color:var(--ink)}
.states h2 em{font-family:"Source Sans 3",Arial,sans-serif;font-weight:400;font-style:italic;text-transform:lowercase;color:var(--blue)}
.state-cols{position:absolute;left:140px;top:176px;width:940px;display:grid;grid-template-columns:repeat(5,1fr);font-size:16px;line-height:27px;color:#3c4146}
.state-cols ul{list-style:none}

/* programs */
.programs{top:2560px;height:710px;background:var(--dark)}
.programs h2{margin-top:72px;font-size:40px;color:var(--white)}
.program-cols{position:absolute;top:176px;left:100px;width:1000px;display:grid;grid-template-columns:repeat(4,1fr);text-align:center}
.program svg{height:58px}
.program h3{font-family:"Source Sans 3",Arial,sans-serif;font-weight:400;font-size:32px;line-height:34px;color:var(--white);margin:12px 0 40px}
.program ul{list-style:none;font-family:"Montserrat",Arial,sans-serif;font-size:14px;line-height:32px;color:var(--dark-text);letter-spacing:.3px}

/* footer */
.site-footer{top:3270px;height:126px;background:var(--footer);text-align:center;font-family:"Montserrat",Arial,sans-serif;font-size:13px;color:#45494d;letter-spacing:.4px}
.site-footer p:first-child{margin-top:40px}
.site-footer p+p{margin-top:14px}
</style>
</head>
<body>

<header class="site-header">
  <div class="logo">LOGO<br>HERE</div>
  <div class="social"><span></span><span></span><span></span></div>
  <nav class="main-nav">
    <a href="#">HOME</a>
    <a href="#" class="has-sub">STATES</a>
    <a href="#" class="has-sub">PROGRAMS</a>
    <a href="#" class="has-sub">DEGREES</a>
    <a href="#">ACCREDITATION</a>
    <a href="#">RANKINGS</a>
    <a href="#">RESOURCES</a>
  </nav>
</header>

<section class="definition">
  <div class="word">
    <h1>ac·cred·it·ed</h1>
    <div class="say">[uh-kred-i-tid]</div>
    <div class="pos">adjective</div>
  </div>
  <ol class="senses">
    <li>1. A college, schools, or online programs that has been officially reviewed to ensure it meets rigorous education standards and qualifies for federal financial assistance</li>
    <li>2. Term that you will better understand after exploring AccredHub Online</li>
  </ol>
</section>

<section class="features">
  <svg class="band" width="1200" height="500" viewBox="0 0 1200 500">
    <defs>
      <linearGradient id="bandFill" x1="0" y1="0" x2="0" y2="1">
        <stop offset="0" stop-color="#1fa2f2"/>
        <stop offset="1" stop-color="#0e88de"/>
      </linearGradient>
    </defs>
    <path d="M0 40 Q600 150 1200 40 L1200 500 L0 500 Z" fill="url(#bandFill)"/>
    <path d="M0 40 Q600 150 1200 40 L1200 70 Q600 170 0 70 Z" fill="#7cc8f7" opacity=".45"/>
  </svg>
  <div class="feature-row">
    <div class="feature">
      <svg viewBox="0 0 64 64" fill="none" stroke="#fff" stroke-width="4"><rect x="10" y="14" width="40" height="26" rx="4" transform="rotate(-30 30 27)"/><circle cx="44" cy="44" r="8" fill="#fff"/><path d="M40 50 l-2 12 6-4 6 4-2-12"/></svg>
      <h3>RANKINGS</h3>
      <p>Explore ranked schools side by side and compare outcomes, tuition and support services before choosing.</p>
      <a class="btn btn-white" href="#">LEARN MORE</a>
    </div>
    <div class="feature">
      <svg viewBox="0 0 64 64" fill="#fff"><path d="M32 10 62 24 32 38 2 24Z"/><path d="M14 32v12c0 6 36 6 36 0V32L32 40Z"/><rect x="56" y="24" width="3" height="20"/></svg>
      <h3>ACCREDITATION</h3>
      <p>Learn how accreditation works, who grants it and why it matters for credits, aid and future careers.</p>
      <a class="btn btn-white" href="#">LEARN MORE</a>
    </div>
    <div class="feature">
      <svg viewBox="0 0 64 64" fill="#fff"><path d="M32 4 60 18H4Z"/><rect x="8" y="22" width="48" height="4"/><rect x="12" y="30" width="6" height="22"/><rect x="24" y="30" width="6" height="22"/><rect x="36" y="30" width="6" height="22"/><rect x="48" y="30" width="6" height="22"/><rect x="4" y="56" width="56" height="5"/></svg>
      <h3>RESOURCES</h3>
      <p>Guides, checklists and tools that help students plan applications, financial aid and transfer paths.</p>
      <a class="btn btn-white" href="#">LEARN MORE</a>
    </div>
  </div>
</section>

<section class="video">
  <h2>VIDEO PARAGRAPH</h2>
  <p class="video-text">Watch this short overview to see how accreditation protects students and how our directory helps you find trusted programs. We explain the review process, the agencies involved, and what to look for on any school website before you apply, enroll or transfer credits between colleges.</p>
  <div class="player">
    <div class="still" role="img" aria-label="Video still of a desk with books and a laptop"></div>
    <div class="play"></div>
    <div class="controls"><div class="track"><i></i></div><div class="knob"></div><div class="vol"></div><div class="full"></div></div>
  </div>
</section>

<section class="trust">
  <div class="label">TRUST</div>
  <div class="badge" style="left:300px;width:110px"></div>
  <div class="badge" style="left:490px;width:150px"></div>
  <div class="badge" style="left:760px;width:150px"></div>
  <div class="badge" style="left:960px;width:100px"></div>
</section>

<section class="paragraphs">
  <h2>PARAGRAPHS TITLE</h2>
  <div class="copy">
    <p>Choosing a college is one of the biggest decisions a student will make, and accreditation is the first signal that a school meets accepted standards. Regional and national agencies review faculty, curriculum, student services and finances on a regular cycle. Schools that pass earn the right to offer federal aid and their credits are far more likely to transfer to other institutions later on.</p>
    <p>Before you apply, confirm the accrediting body is recognized and check whether your program has its own specialized approval. Nursing, business and law degrees often require it for licensure. Our directory lists each school's status so you can compare options quickly and focus on programs that fit your goals.</p>
  </div>
  <a class="btn btn-outline" href="#">READ MORE</a>
</section>

<section class="states">
  <div class="map" role="img" aria-label="Map of the United States"></div>
  <h2>SEARCH COLLEGES <em>by</em> STATE</h2>
  <div class="state-cols">
    <ul><li>Alabama</li><li>Alaska</li><li>Arizona</li><li>Arkansas</li><li>California</li><li>Colorado</li><li>Connecticut</li><li>Delaware</li><li>Florida</li><li>Georgia</li></ul>
    <ul><li>Hawaii</li><li>Idaho</li><li>Illinois</li><li>Indiana</li><li>Iowa</li><li>Kansas</li><li>Kentucky</li><li>Louisiana</li><li>Maine</li><li>Maryland</li></ul>
    <ul><li>Massachusetts</li><li>Michigan</li><li>Minnesota</li><li>Mississippi</li><li>Missouri</li><li>Montana</li><li>Nebraska</li><li>Nevada</li><li>New Hampshire</li><li>New Jersey</li></ul>
    <ul><li>New Mexico</li><li>New York</li><li>North Carolina</li><li>North Dakota</li><li>Ohio</li><li>Oklahoma</li><li>Oregon</li><li>Pennsylvania</li><li>Rhode Island</li><li>South Carolina</li></ul>
    <ul><li>South Dakota</li><li>Tennessee</li><li>Texas</li><li>Utah</li><li>Vermont</li><li>Virginia</li><li>Washington</li><li>West Virginia</li><li>Wisconsin</li><li>Wyoming</li></ul>
  </div>
</section>

<section class="programs">
  <h2>OUR PROGRAMS</h2>
  <div class="program-cols">
    <div class="program">
      <svg viewBox="0 0 64 58" fill="#1a9bef"><rect x="2" y="10" width="40" height="40" rx="4"/><rect x="30" y="4" width="32" height="50" rx="4"/><rect x="35" y="10" width="22" height="10" fill="#333538"/><circle cx="22" cy="30" r="10" fill="#333538"/></svg>
      <h3>Accounting<br>Programs</h3>
      <ul><li>ACCOUNTING</li><li>ART</li><li>BIBLE</li><li>BUSINESS</li><li>CRIMINAL JUSTICE</li><li>DESIGN</li><li>EDUCATION</li></ul>
    </div>
    <div class="program">
      <svg viewBox="0 0 64 58" fill="#1a9bef"><path d="M32 2 60 16H4Z"/><rect x="8" y="19" width="48" height="4"/><rect x="12" y="26" width="6" height="20"/><rect x="24" y="26" width="6" height="20"/><rect x="36" y="26" width="6" height="20"/><rect x="48" y="26" width="6" height="20"/><rect x="4" y="50" width="56" height="6"/></svg>
      <h3>Law<br>Programs</h3>
      <ul><li>ENGINEERING</li><li>ENGLISH</li><li>LAW</li><li>LPN TO RN</li><li>MANAGEMENT</li><li>MATH</li><li>MBA</li></ul>
    </div>
    <div class="program">
      <svg viewBox="0 0 64 58" fill="#1a9bef"><rect x="4" y="14" width="56" height="40" rx="5"/><path d="M22 14V8h20v6h-5v-2H27v2Z"/><rect x="4" y="30" width="56" height="3" fill="#333538"/><rect x="28" y="27" width="8" height="9" rx="1"/></svg>
      <h3>MBA<br>Programs</h3>
      <ul><li>MPH</li><li>MEDICAL ASSISTING</li><li>MILITARY</li><li>NURSING</li><li>OCCUPATIONAL THERAPY</li><li>PARALEGAL</li><li>PSYCHOLOGY</li></ul>
    </div>
    <div class="program">
      <svg viewBox="0 0 64 58" fill="#1a9bef"><circle cx="32" cy="29" r="27"/><path d="M27 14h10v10h10v10H37v10H27V34H17V24h10Z" fill="#333538"/></svg>
      <h3>Nursing<br>Programs</h3>
      <ul><li>PHARMACY</li><li>RN TO BSN</li><li>RADIOLOGY</li><li>SOCIAL WORK</li><li>SONOGRAPHY</li></ul>
    </div>
  </div>
</section>

<footer class="site-footer">
  <p>COPYRIGHT © 2015 WWW.ACCREDHUB.ORG. ALL RIGHTS RESERVED.</p>
  <p><a href="#">ABOUT US</a> · <a href="#">PRIVACY</a></p>
</footer>

</body>
</html>
```